BrightHarbor is a fund management company that takes just four market positions a year. each position is linked to a big geopolitical and economic event happening in the world. So for example we may be buying gold mining stocks-these are the companies who dig the gold out of the ground, as all the gold is currently being bought by Asia, or buying the japanese stock market as this is one of the big stories of today.

I am looking for a logo that represents 'BrightHarbor'-the Bright Harbor.

I would like it to be small and sit to the left of the name of the company on the left hand side(I think!)on the top line of the business card please.

Industry/Entity Type

Mining

Contact Information for Business Card

BrightHarbor Investment management Ltd
41 Fennick Lane
London E9 7QT

Tomas P Hulme

Mob: 0(44)7839254086
Off: 0(44) 203 xxxx
email: th@brightharbor-fm.example

```html
<!DOCTYPE html>
<html lang="en">
<head>
<meta charset="utf-8">
<title>BrightHarbor business cards</title>
<link rel="stylesheet" href="https://fonts.googleapis.com/css2?family=Arimo&family=Caladea:wght@700&display=swap">
<style>
  :root {
    --backdrop: #bdbec0;
    --card: #ffffff;
    --card-edge: #d4d4d6;
    --ink: #1f1f1f;
    --brand-navy: #2b2a6e;
    --brand-sky: #29a6cf;
  }
  * { margin: 0; padding: 0; box-sizing: border-box; }
  html, body { width: 1200px; height: 1200px; overflow: hidden; }
  body { background: var(--backdrop); position: relative; }

  .business-card {
    position: absolute;
    left: 255px;
    width: 690px;
    height: 393px;
    background: var(--card);
    border: 1px solid var(--card-edge);
    color: var(--ink);
  }
  .business-card--first { top: 131px; }
  .business-card--second { top: 664px; }

  .brand-mark {
    position: absolute;
    left: 56px;
    top: 63px;
    display: flex;
    align-items: center;
    gap: 8px;
  }
  .brand-mark__dot {
    width: 40px; height: 40px;
    border-radius: 50%;
    background: var(--brand-sky);
  }
  .brand-mark__name {
    font-family: "Caladea", serif;
    font-weight: 700;
    font-size: 21px;
    color: var(--brand-navy);
  }

  .company-name {
    position: absolute;
    right: 60px;
    top: 71px;
    font-family: "Caladea", serif;
    font-weight: 700;
    font-size: 19px;
    color: #111;
    white-space: nowrap;
  }

  .person-name {
    position: absolute;
    left: 0; right: 0;
    top: 161px;
    text-align: center;
    padding-left: 40px;
    font-family: "Arimo", sans-serif;
    font-size: 23px;
  }

  .contact-list {
    position: absolute;
    left: 0;
    top: 219px;
    display: grid;
    grid-template-columns: 99px auto;
    column-gap: 25px;
    row-gap: 4px;
    font-family: "Arimo", sans-serif;
    font-size: 21px;
    line-height: 26px;
  }
  .contact-list dt {
    text-align: right;
    font-family: "Caladea", serif;
    font-weight: 700;
    font-size: 20px;
  }
  .contact-list dd { white-space: nowrap; }
</style>
</head>
<body>

  <section class="business-card business-card--first">
    <div class="brand-mark">
      <span class="brand-mark__dot"></span>
      <span class="brand-mark__name">BrightHarbor</span>
    </div>
    <p class="company-name">BrightHarbor Investment Managment Ltd</p>
    <p class="person-name">Tomas P Hulme</p>
    <dl class="contact-list">
      <dt>a:</dt><dd>41 Fennick Lane, London<br>E9 7QT</dd>
      <dt>mob:</dt><dd>0(44) 783 925 4086</dd>
      <dt>off:</dt><dd>0(44) 203 618 2704</dd>
      <dt>e:</dt><dd>th@brightharbor-fm.example</dd>
    </dl>
  </section>

  <section class="business-card business-card--second">
    <div class="brand-mark">
      <span class="brand-mark__dot"></span>
      <span class="brand-mark__name">BrightHarbor</span>
    </div>
    <p class="company-name">BrightHarbor Investment Managment Ltd</p>
    <p class="person-name">Tomas P Hulme</p>
    <dl class="contact-list">
      <dt>a:</dt><dd>41 Fennick Lane, London<br>E9 7QT</dd>
      <dt>mob:</dt><dd>0(44) 783 925 4086</dd>
      <dt>off:</dt><dd>0(44) 203 618 2704</dd>
      <dt>e:</dt><dd>th@brightharbor-fm.example</dd>
    </dl>
  </section>

</body>
</html>
```